Harborline Stay Collective Business Card Design

Design a business card for Harborline Stay Collective. Look at the website for colors and reference. Card should have logo, name, title, office number, mobile number, email, URL and a tagline like, "Luxury Hotel & Resort Email Marketing" (This might change).

https://www.harborlinestaycollective.net

The rest I will leave up to your imagination.

Contact Information for Business Card

Logo, name, title, office number, mobile number, email, URL and a tagline like, "Luxury Hotel & Resort Email Marketing" (This might change).

```html
<!DOCTYPE html>
<html lang="en">
<head>
<meta charset="utf-8">
<title>Harborline Stay Collective – Business Card</title>
<link href="https://fonts.googleapis.com/css2?family=Exo+2:wght@400;500;700&display=swap" rel="stylesheet">
<style>
  :root {
    --stage: #272427;
    --ink: #060708;
    --orange: #f37021;
    --paper: #ffffff;
    --text: #0b0b0c;
    --coast-top: #2f3f4a;
    --coast-mid: #3d5046;
    --coast-low: #1f5a5a;
    --office-a: #5d6e80;
    --office-b: #3c4654;
  }
  * { box-sizing: border-box; margin: 0; padding: 0; }
  html, body { width: 1200px; height: 1200px; overflow: hidden; }
  body {
    background: var(--stage);
    font-family: "Exo 2", sans-serif;
    position: relative;
  }
  .card {
    position: absolute;
    left: 180px;
    width: 840px;
    height: 480px;
    background: var(--ink);
    overflow: hidden;
  }
  .card--front { top: 90px; }
  .card--back { top: 630px; }

  /* Front card */
  .front-photo {
    position: absolute;
    left: 28px; top: 28px; right: 28px; bottom: 28px;
    background: linear-gradient(175deg, var(--coast-top) 0%, var(--coast-top) 30%, var(--coast-mid) 55%, var(--coast-low) 75%, #2c3a30 100%);
  }
  .front-frame {
    position: absolute; background: var(--orange);
  }
  .frame-top { left: 270px; top: 28px; width: 542px; height: 8px; }
  .frame-right { right: 28px; top: 28px; width: 8px; height: 340px; }
  .frame-bottom { left: 28px; bottom: 28px; width: 420px; height: 8px; }
  .frame-left { left: 28px; bottom: 28px; width: 8px; height: 250px; }
  .front-brand {
    position: absolute;
    left: 0; right: 0; top: 200px;
    display: flex; align-items: center; justify-content: center; gap: 16px;
  }
  .brand-square {
    width: 26px; height: 26px; background: var(--orange);
  }
  .front-brand .brand-name {
    color: var(--paper);
    font-weight: 700;
    font-size: 44px;
    letter-spacing: 1px;
    text-transform: uppercase;
  }

  /* Back card */
  .band { position: absolute; background: var(--orange); }
  .band-top { left: 18px; top: 60px; width: 452px; height: 30px; }
  .band-left { left: 18px; top: 60px; width: 30px; height: 402px; }
  .band-bottom { left: 18px; top: 430px; width: 560px; height: 32px; }
  .panel {
    position: absolute; left: 48px; top: 90px; width: 600px; height: 340px;
    background: var(--paper);
  }
  .panel-cap {
    position: absolute; left: 470px; top: 60px; width: 178px; height: 30px;
    background: var(--paper);
  }
  .photo-strip {
    position: absolute; left: 648px; top: 30px; width: 172px; height: 420px;
    display: flex; flex-direction: column; gap: 8px;
  }
  .photo-strip .shot { flex: 1; }
  .shot--mail { background: linear-gradient(160deg, #a9bccc, var(--office-a)); }
  .shot--data { background: linear-gradient(160deg, #7b8ea3, var(--office-b)); }
  .shot--design { background: linear-gradient(160deg, #8fa3b6, #3f4b58); }

  .service {
    position: absolute; left: 598px;
    width: 100px; height: 100px; border-radius: 50%;
    background: var(--paper);
    border: 9px solid var(--orange);
    display: flex; flex-direction: column; align-items: center; justify-content: center;
    gap: 3px;
  }
  .service svg { width: 34px; height: 34px; }
  .service-label {
    color: var(--orange); font-size: 7.5px; text-align: center; line-height: 1.15;
    text-transform: uppercase; font-weight: 500;
  }
  .service--1 { top: 100px; }
  .service--2 { top: 215px; }
  .service--3 { top: 330px; }

  .back-brand {
    position: absolute; left: 100px; top: 125px;
    display: flex; align-items: center; gap: 10px;
  }
  .back-brand .brand-square { width: 18px; height: 18px; }
  .back-brand .brand-name {
    color: var(--text); font-weight: 700; font-size: 24px; text-transform: uppercase;
  }
  .person-name {
    position: absolute; left: 100px; top: 190px;
    font-weight: 700; font-size: 34px; color: var(--text); text-transform: uppercase;
  }
  .person-title {
    position: absolute; left: 104px; top: 234px;
    font-size: 22px; color: var(--orange);
  }
  .contacts {
    position: absolute; left: 110px; top: 285px;
    list-style: none;
  }
  .contacts li {
    display: flex; align-items: center; gap: 14px;
    font-size: 19px; color: var(--text); height: 32px;
  }
  .contacts svg { width: 20px; height: 20px; flex: none; }
</style>
</head>
<body>

<section class="card card--front" aria-label="Card front">
  <div class="front-photo" role="img" aria-label="Coastal resort landscape with pine-covered headland and turquoise sea, darkened"></div>
  <div class="front-frame frame-top"></div>
  <div class="front-frame frame-right"></div>
  <div class="front-frame frame-bottom"></div>
  <div class="front-frame frame-left"></div>
  <div class="front-brand">
    <span class="brand-square"></span>
    <span class="brand-name">Harborline Stay Collective</span>
  </div>
</section>

<section class="card card--back" aria-label="Card back">
  <div class="band band-top"></div>
  <div class="band band-left"></div>
  <div class="band band-bottom"></div>
  <div class="panel"></div>
  <div class="panel-cap"></div>

  <div class="photo-strip">
    <div class="shot shot--mail" role="img" aria-label="Office desk with email marketing graphics"></div>
    <div class="shot shot--data" role="img" aria-label="Laptop showing analytics dashboards"></div>
    <div class="shot shot--design" role="img" aria-label="Hand holding a printed letter design against city buildings"></div>
  </div>

  <div class="service service--1">
    <svg viewBox="0 0 34 34" fill="none" stroke="#111" stroke-width="1.4" stroke-linejoin="round">
      <path d="M4 14 L17 6 L30 14 V29 H4 Z"/><path d="M4 14 L17 22 L30 14"/><path d="M4 29 L14 20 M30 29 L20 20"/>
      <path d="M19 5 L27 2 V11 L19 8 Z"/>
    </svg>
    <span class="service-label">Email Marketing<br>Service</span>
  </div>
  <div class="service service--2">
    <svg viewBox="0 0 34 34" fill="none" stroke="#111" stroke-width="1.4">
      <path d="M7 3 H22 L27 8 V30 H7 Z"/><path d="M11 14 H18 M11 18 H16 M11 22 H17 M11 9 L15 7 L18 10 L22 6"/>
      <circle cx="23" cy="22" r="5"/><path d="M26.5 25.5 L31 30"/><path d="M21 22 L22.5 23.5 L25 20.5"/>
    </svg>
    <span class="service-label">Data &amp; Results<br>Service</span>
  </div>
  <div class="service service--3">
    <svg viewBox="0 0 34 34" fill="none" stroke="#111" stroke-width="1.4">
      <rect x="5" y="5" width="24" height="24"/><path d="M11 25 L17 9 L23 25 M13.5 19 H20.5"/>
      <rect x="3" y="3" width="4" height="4" fill="#fff"/><rect x="27" y="3" width="4" height="4" fill="#fff"/>
      <rect x="3" y="27" width="4" height="4" fill="#fff"/><rect x="27" y="27" width="4" height="4" fill="#fff"/>
    </svg>
    <span class="service-label">Email Ads Design<br>Service</span>
  </div>

  <div class="back-brand">
    <span class="brand-square"></span>
    <span class="brand-name">Harborline Stay Collective</span>
  </div>
  <h1 class="person-name">Dana Whitford</h1>
  <p class="person-title">Account Manager</p>

  <ul class="contacts">
    <li>
      <svg viewBox="0 0 20 20" fill="none" stroke="#111" stroke-width="1.3"><circle cx="10" cy="10" r="8.5"/><path d="M7 5.5 L8.5 8 L7.5 9 Q9 12 11 12.5 L12 11.5 L14.5 13 L13.5 14.5 Q8 15 5.5 7 Z"/></svg>
      <span>0555-01234-777</span>
    </li>
    <li>
      <svg viewBox="0 0 20 20" fill="none" stroke="#111" stroke-width="1.3"><rect x="2" y="5" width="16" height="11"/><path d="M2 5 L10 11 L18 5 M2 16 L8 10 M18 16 L12 10"/></svg>
      <span>mail@yoursite.com</span>
    </li>
    <li>
      <svg viewBox="0 0 20 20" fill="none" stroke="#111" stroke-width="1.3"><circle cx="10" cy="10" r="8.5"/><ellipse cx="10" cy="10" rx="3.8" ry="8.5"/><path d="M1.5 10 H18.5 M3 5.5 H17 M3 14.5 H17"/></svg>
      <span>www.yoursite.com</span>
    </li>
    <li>
      <svg viewBox="0 0 20 20" fill="none" stroke="#111" stroke-width="1.3"><path d="M10 15 C6 10 5 8.5 5 6.5 A5 5 0 0 1 15 6.5 C15 8.5 14 10 10 15 Z"/><circle cx="10" cy="6.5" r="1.8"/><path d="M6 13 L2 18 H18 L14 13"/></svg>
      <span>Lorem lipsum dolor sit amet</span>
    </li>
  </ul>
</section>

</body>
</html>
```